Postcard Design

I have an accounting firm and I would like to increase my customer base by a postcard mailout/letter dropI want a design that is eye catching and uses my logo. I specialise in small to medium business and offer services for commercial accounting and business advisory. I also want to offer a discount for new clients.Previously I had my website updated and would like to stay with the theme

Industry/Entity Type

Business Consultant

Font styles to use
Serif

Colors
b667aa
d3a5cc

Requirements
Must have
• the post card needs to be arty to attract attention. also business like

```html
<!DOCTYPE html>
<html lang="en">
<head>
<meta charset="utf-8">
<title>Corvell Accounting Services – Postcard</title>
<link href="https://fonts.googleapis.com/css2?family=Open+Sans:ital,wght@0,400;0,600;0,700;0,800;1,700;1,800&family=Arimo:wght@400;700&display=swap" rel="stylesheet">
<style>
  :root{
    --backdrop:#a7a8ab;
    --purple:#a3559e;
    --purple-light:#d3a5cc;
    --teal:#4ea19a;
    --teal-dark:#3f8e88;
    --ink:#111111;
    --paper:#ffffff;
  }
  *{box-sizing:border-box;margin:0;padding:0}
  html,body{width:1200px;height:741px;overflow:hidden;background:var(--backdrop)}
  .postcard{
    position:absolute;left:100px;top:90px;width:1000px;height:560px;
    background:var(--paper);overflow:hidden;
    box-shadow:0 6px 18px rgba(0,0,0,.25);
    font-family:"Open Sans",Arial,sans-serif;
  }
  .headline-panel{
    position:absolute;left:0;top:0;width:420px;height:150px;background:var(--purple);
    color:#fff;padding:20px 24px;
  }
  .headline-panel .services{font-weight:800;font-style:italic;font-size:27px;line-height:1.05}
  .headline-panel .services span{display:block;font-size:21px;padding-left:4px}
  .headline-panel .motto{font-weight:600;font-size:24px;line-height:1.1;margin-top:6px;padding-left:8px}
  .strengths-panel{
    position:absolute;left:0;top:150px;width:420px;height:190px;background:var(--teal);
    color:#fff;padding:22px 24px;
  }
  .strengths-panel ul{list-style:none}
  .strengths-panel li{font-size:17px;font-weight:600;line-height:1.15;margin-bottom:4px;padding-left:20px;position:relative}
  .strengths-panel li svg{position:absolute;left:0;top:4px}
  .photo{position:absolute;left:420px;width:580px}
  .photo-calculator{top:0;height:150px;background:linear-gradient(100deg,#c9cdd3 0%,#eef0f3 45%,#dfe3e8 100%)}
  .photo-meeting{top:150px;height:190px;background:linear-gradient(100deg,#4b5566 0%,#b9c1cc 40%,#e8ecef 75%,#d9dee3 100%)}
  .tab{position:absolute;right:0;width:230px;height:120px}
  .tab-excellence{top:0}
  .tab-advice{top:130px}
  .tab .label{
    position:absolute;right:0;top:0;width:230px;height:60px;
    color:#fff;font-size:14px;line-height:1.1;text-align:center;padding-top:10px;
  }
  .tab svg{position:absolute;left:0;top:0}
  .contact-band{position:absolute;left:0;top:340px;width:1000px;height:220px;background:var(--paper)}
  .logo-dot{position:absolute;left:60px;top:50px;width:120px;height:120px;border-radius:50%;background:var(--purple)}
  .contact{position:absolute;left:215px;top:42px;font-family:"Arimo",Arial,sans-serif}
  .firm-name{font-size:24px;font-weight:700;color:var(--ink)}
  .phone{font-size:56px;color:var(--teal);line-height:1.05}
  .web{font-size:20px;font-weight:700;color:var(--purple)}
  .offer{
    position:absolute;right:40px;top:20px;width:340px;height:165px;
    border:5px solid var(--purple);padding:8px;
  }
  .offer-inner{
    width:100%;height:100%;border:4px solid var(--teal);
    display:flex;flex-direction:column;justify-content:center;padding-left:14px;color:var(--ink);
  }
  .offer .line-1{font-size:46px;font-weight:400;line-height:.95;letter-spacing:-1px}
  .offer .line-2{font-size:46px;font-weight:800;line-height:.95;letter-spacing:-1px}
  .offer .line-3{font-size:25px;font-weight:400;line-height:1.1}
</style>
</head>
<body>
<main class="postcard">
  <section class="headline-panel">
    <h1 class="services">Business Advisory &amp;<span>Commercial Accountants</span></h1>
    <p class="motto">We Believe in Exercising<br>Professional Integrity</p>
  </section>

  <section class="strengths-panel">
    <ul>
      <li><svg width="12" height="12" viewBox="0 0 12 12"><path d="M1 6l3 3 7-7" stroke="#fff" stroke-width="2.2" fill="none"/></svg>Committed to Innovative Accounting Strategies</li>
      <li><svg width="12" height="12" viewBox="0 0 12 12"><path d="M1 6l3 3 7-7" stroke="#fff" stroke-width="2.2" fill="none"/></svg>Professionally Qualified Accountants</li>
      <li><svg width="12" height="12" viewBox="0 0 12 12"><path d="M1 6l3 3 7-7" stroke="#fff" stroke-width="2.2" fill="none"/></svg>Proactively Deliver Services</li>
      <li><svg width="12" height="12" viewBox="0 0 12 12"><path d="M1 6l3 3 7-7" stroke="#fff" stroke-width="2.2" fill="none"/></svg>Support Our Clients in Achieving Business Goals</li>
    </ul>
  </section>

  <div class="photo photo-calculator" role="img" aria-label="Photo of a hand using a calculator over financial spreadsheets"></div>
  <div class="photo photo-meeting" role="img" aria-label="Photo of business people in a meeting reviewing documents"></div>

  <div class="tab tab-excellence">
    <svg width="230" height="120" viewBox="0 0 230 120">
      <path d="M20 0H230V60H80L60 44H20Z" fill="var(--teal)"/>
      <circle cx="100" cy="88" r="26" fill="var(--teal)"/>
      <rect x="90" y="76" width="16" height="22" rx="2" fill="#fff"/>
      <rect x="93" y="79" width="10" height="5" fill="var(--teal)"/>
      <circle cx="110" cy="96" r="6" fill="#fff" stroke="var(--teal)" stroke-width="2"/>
    </svg>
    <p class="label">Committed to<br>Excellence</p>
  </div>

  <div class="tab tab-advice">
    <svg width="230" height="120" viewBox="0 0 230 120">
      <path d="M20 0H230V60H80L60 44H20Z" fill="var(--teal)"/>
      <circle cx="100" cy="88" r="26" fill="var(--teal)"/>
      <rect x="90" y="76" width="16" height="22" rx="2" fill="#fff"/>
      <rect x="93" y="79" width="10" height="5" fill="var(--teal)"/>
      <circle cx="110" cy="96" r="6" fill="#fff" stroke="var(--teal)" stroke-width="2"/>
    </svg>
    <p class="label">Sound Business<br>Advice</p>
  </div>

  <section class="contact-band">
    <div class="logo-dot"></div>
    <div class="contact">
      <p class="firm-name">Corvell Accounting Services</p>
      <p class="phone">02 4000 5173</p>
      <p class="web">www.CorvellAccountingServices.com</p>
    </div>
    <div class="offer">
      <div class="offer-inner">
        <p class="line-1">OFFERING</p>
        <p class="line-2">DISCOUNTS</p>
        <p class="line-3">FOR NEW CLIENTS</p>
      </div>
    </div>
  </section>
</main>
</body>
</html>
```